Design a helpdesk ticketing platform *

We are launching a helpdesk ticketing platform. Very much like lumidesk.example, brightowl.example, calmhub.example, tidyqueue.example etc. We have a full mid-fidelity prototype built and we want someone to build the full fidelity of the product.

You can view the full mid-fidelity prototype here: https://shortlink.example/Qw8pLk

The best way moving forward is to just design the following 4 pages

- Main Dashboard https://shortlink.example/48vRxN
- All tickets https://shortlink.example/jbdYsW
- Viewing a ticket https://shortlink.example/mHqLtB
- Contacts https://shortlink.example/yKeoPd

Target Market(s)

Small business owners

Industry/Entity Type

Saas

Number of Pages Required

4 page

Font styles to use
Serif
Sans Serif

Colors

Designer to choose colors to be used in the design.

Requirements
Must have
• Must follow the prototype exactly. We are not looking for any UX changes. We want the designe xactly as the prototype is. We are only looking for design ideas.
Should not have
• modern, clean. We'd love to see the primary color as yellow, purple, orange, green or blue. You choose which one you think looks best and go with that.

```html
<!DOCTYPE html>
<html lang="en">
<head>
<meta charset="utf-8">
<title>ticketnest – Dashboard</title>
<link href="https://fonts.googleapis.com/css2?family=Roboto:wght@400;500;700&display=swap" rel="stylesheet">
<style>
  :root {
    --sidebar: #031b30;
    --brand-blue: #2b96e0;
    --page-bg: #e9f4fb;
    --white: #ffffff;
    --teal: #26a69a;
    --pink: #ec407a;
    --sky: #29b6f6;
    --mustard: #c5820e;
    --orange: #f5a623;
    --activity-bar: #0a7fb8;
    --text-dark: #333a40;
    --text-muted: #555d63;
    --rule: #d6d6d6;
    --icon-green: #2ea84f;
    --icon-yellow: #c8b820;
  }
  * { box-sizing: border-box; margin: 0; padding: 0; }
  html, body { width: 950px; height: 1200px; overflow: hidden; }
  body { position: relative; background: var(--page-bg); font-family: "Roboto", sans-serif; color: var(--text-dark); }

  .sidebar { position: absolute; left: 0; top: 0; width: 255px; height: 1200px; background: var(--sidebar); }
  .brand-bar { position: absolute; left: 0; top: 0; width: 255px; height: 51px; background: var(--brand-blue); }
  .brand-name { position: absolute; left: 43px; top: 12px; font-size: 21px; color: var(--white); letter-spacing: .5px; }
  .menu-toggle { position: absolute; left: 221px; top: 16px; }

  .new-ticket { position: absolute; left: 44px; top: 86px; width: 158px; height: 24px; background: var(--orange); color: var(--white); font-size: 11px; font-weight: 500; line-height: 24px; padding-left: 6px; }
  .new-ticket .dots { position: absolute; right: 6px; top: 4px; }

  .nav-item { position: absolute; left: 44px; width: 158px; height: 20px; font-size: 11px; color: var(--white); letter-spacing: .5px; line-height: 20px; }
  .nav-item .label { position: absolute; left: 33px; }
  .nav-item svg { position: absolute; left: 4px; top: 2px; }
  .nav-item.active { background: var(--white); color: var(--text-dark); }
  .nav-item .caret { position: absolute; right: 0; top: 8px; left: auto; }
  .sub-item { position: absolute; left: 91px; font-size: 10px; color: var(--white); }
  .sub-rule { position: absolute; left: 83px; top: 289px; width: 109px; height: 1px; background: #2a3d50; }

  .topbar { position: absolute; left: 255px; top: 0; width: 695px; height: 51px; background: var(--white); box-shadow: 0 1px 2px rgba(0,0,0,.15); }
  .page-title { position: absolute; left: 28px; top: 20px; font-size: 10px; letter-spacing: .5px; color: var(--text-dark); }
  .search { position: absolute; left: 447px; top: 22px; width: 180px; height: 15px; border-bottom: 1px solid #c9c9c9; }
  .search svg { position: absolute; right: 0; top: 1px; }

  .avatar { position: absolute; left: 283px; top: 72px; width: 72px; height: 72px; border-radius: 50%; border: 2px solid var(--teal); background: radial-gradient(circle at 50% 40%, #d9c3b0, #8d8a86 70%, #e5e5e5); }
  .greeting { position: absolute; left: 370px; top: 89px; font-size: 12px; color: var(--text-muted); }
  .user-name { position: absolute; left: 370px; top: 104px; font-size: 22px; font-weight: 500; letter-spacing: 1.5px; color: #1d2328; }

  .stat-tile { position: absolute; height: 182px; color: var(--white); text-align: center; box-shadow: 2px 3px 3px rgba(0,0,0,.25); }
  .stat-tile .count { position: absolute; left: 0; right: 0; top: 50px; font-size: 48px; font-weight: 500; line-height: 1; letter-spacing: 2px; }
  .stat-tile .caption { position: absolute; left: 0; right: 0; top: 103px; font-size: 18px; font-weight: 500; letter-spacing: .5px; }
  .teal { background: var(--teal); } .pink { background: var(--pink); } .sky { background: var(--sky); } .mustard { background: var(--mustard); }
  .mustard .caption { font-weight: 400; }

  .activity-bar { position: absolute; left: 283px; top: 574px; width: 599px; height: 46px; background: var(--activity-bar); color: var(--white); font-size: 16px; font-weight: 500; line-height: 46px; padding-left: 25px; box-shadow: 0 2px 3px rgba(0,0,0,.2); }

  .activity-card { position: absolute; left: 283px; width: 599px; height: 215px; background: var(--white); border: 1px solid #d0d0d0; box-shadow: 0 1px 3px rgba(0,0,0,.2); }
  .activity-card h3 { position: absolute; left: 24px; top: 19px; font-size: 13px; font-weight: 400; color: var(--text-muted); }
  .activity-card .rule { position: absolute; left: 4px; right: 4px; top: 41px; height: 1px; background: var(--rule); }
  .activity-row { position: absolute; left: 25px; right: 25px; height: 26px; }
  .activity-row .initial { position: absolute; left: 0; top: 0; width: 26px; height: 26px; border-radius: 50%; color: var(--white); font-size: 10px; line-height: 26px; text-align: center; }
  .activity-row .message { position: absolute; left: 44px; top: 6px; font-size: 10px; color: var(--text-dark); letter-spacing: .2px; }
  .activity-row .time { position: absolute; right: 0; top: 7px; font-size: 10px; color: var(--text-dark); }

  .load-more { position: absolute; left: 504px; top: 1125px; width: 158px; height: 26px; background: var(--sidebar); color: var(--white); font-size: 10px; font-weight: 500; letter-spacing: .5px; text-align: center; line-height: 26px; }
</style>
</head>
<body>
  <aside class="sidebar">
    <div class="brand-bar">
      <div class="brand-name">ticketnest</div>
      <svg class="menu-toggle" width="18" height="16" viewBox="0 0 18 16"><rect y="0" width="18" height="3" fill="#fff"/><rect y="6.5" width="18" height="3" fill="#fff"/><rect y="13" width="18" height="3" fill="#fff"/></svg>
    </div>

    <div class="new-ticket">New Ticket
      <svg class="dots" width="4" height="16" viewBox="0 0 4 16"><circle cx="2" cy="2" r="1.6" fill="#fff"/><circle cx="2" cy="8" r="1.6" fill="#fff"/><circle cx="2" cy="14" r="1.6" fill="#fff"/></svg>
    </div>

    <div class="nav-item active" style="top:129px">
      <svg width="16" height="14" viewBox="0 0 16 14"><path d="M2 12 A7 7 0 1 1 14 12" fill="none" stroke="#26a69a" stroke-width="1.6"/><line x1="8" y1="9" x2="11" y2="5" stroke="#26a69a" stroke-width="1.6"/></svg>
      <span class="label">DASHBOARD</span>
    </div>
    <div class="nav-item" style="top:160px">
      <svg width="18" height="16" viewBox="0 0 18 16"><path d="M2 10 L10 2 L16 2 L16 8 L8 16 Z" fill="none" stroke="#8a96a0" stroke-width="1.2"/><circle cx="13" cy="5" r="1.2" fill="#8a96a0"/></svg>
      <span class="label">TICKETS</span>
      <svg class="caret" width="7" height="4" viewBox="0 0 7 4"><path d="M0 0 L7 0 L3.5 4 Z" fill="#fff"/></svg>
    </div>
    <div class="sub-item" style="top:189px">All tickets</div>
    <div class="sub-item" style="top:214px">My tickets</div>
    <div class="sub-item" style="top:240px">Open tickets</div>
    <div class="sub-item" style="top:265px">Unassigned Tickets</div>
    <div class="sub-rule"></div>
    <div class="sub-item" style="top:299px">Spam</div>
    <div class="sub-item" style="top:324px">Trash</div>

    <div class="nav-item" style="top:364px">
      <svg width="12" height="12" viewBox="0 0 12 12"><circle cx="6" cy="3.5" r="3" fill="var(--icon-yellow)"/><path d="M0 12 Q6 4 12 12 Z" fill="var(--icon-yellow)"/></svg>
      <span class="label">CONTACTS</span>
    </div>
    <div class="nav-item" style="top:410px">
      <svg width="12" height="12" viewBox="0 0 12 12"><circle cx="6" cy="6" r="4.2" fill="none" stroke="#2b96e0" stroke-width="2.6" stroke-dasharray="2 1.3"/><circle cx="6" cy="6" r="2.5" fill="#2b96e0"/><circle cx="6" cy="6" r="1.1" fill="var(--sidebar)"/></svg>
      <span class="label">ADMIN SETTINGS</span>
      <svg class="caret" width="7" height="4" viewBox="0 0 7 4"><path d="M0 0 L7 0 L3.5 4 Z" fill="#fff"/></svg>
    </div>
    <div class="nav-item" style="top:456px">
      <svg width="12" height="16" viewBox="0 0 12 16"><rect x="1" y="2" width="10" height="13" fill="none" stroke="var(--icon-green)" stroke-width="1.4"/><rect x="4" y="0.5" width="4" height="3" fill="var(--icon-green)"/><path d="M3 7h6M3 10h6M3 13h6" stroke="var(--icon-green)" stroke-width="1"/></svg>
      <span class="label">ACCOUNT &amp; BILLING</span>
    </div>
  </aside>

  <header class="topbar">
    <div class="page-title">DASHBOARD</div>
    <div class="search">
      <svg width="10" height="10" viewBox="0 0 10 10"><circle cx="4" cy="4" r="3" fill="none" stroke="#888" stroke-width="1.3"/><line x1="6.3" y1="6.3" x2="9.3" y2="9.3" stroke="#888" stroke-width="1.4"/></svg>
    </div>
  </header>

  <div class="avatar" role="img" aria-label="Profile photo of the signed-in agent"></div>
  <div class="greeting">Good Morning,</div>
  <div class="user-name">Andrew</div>

  <div class="stat-tile teal" style="left:283px;top:166px;width:190px"><div class="count">16</div><div class="caption">Open Tickets</div></div>
  <div class="stat-tile pink" style="left:494px;top:166px;width:179px"><div class="count">14</div><div class="caption">Due Today</div></div>
  <div class="stat-tile sky" style="left:694px;top:166px;width:189px"><div class="count">14</div><div class="caption">Unassigned</div></div>
  <div class="stat-tile sky" style="left:283px;top:369px;width:190px"><div class="count">0</div><div class="caption">Overdue</div></div>
  <div class="stat-tile mustard" style="left:494px;top:369px;width:179px"><div class="count">0</div><div class="caption">On Hold</div></div>
  <div class="stat-tile teal" style="left:694px;top:369px;width:189px"><div class="count">11</div><div class="caption">Not Resolved</div></div>

  <div class="activity-bar">Recent Activities</div>

  <section class="activity-card" style="top:643px">
    <h3>Today</h3>
    <div class="rule"></div>
    <div class="activity-row" style="top:65px"><div class="initial pink">J</div><div class="message">Jammy tan assigned forgot to cc, trying again (#15)to Jeremy Tan</div><div class="time">4.40 pm</div></div>
    <div class="activity-row" style="top:117px"><div class="initial sky">J</div><div class="message">Jammy tan assigned forgot to cc, trying again (#15)to Jeremy Tan</div><div class="time">11.40 am</div></div>
    <div class="activity-row" style="top:168px"><div class="initial mustard">J</div><div class="message">Jammy tan assigned forgot to cc, trying again (#15)to Jeremy Tan</div><div class="time">8.40 am</div></div>
  </section>

  <section class="activity-card" style="top:884px">
    <h3>Yesterday</h3>
    <div class="rule"></div>
    <div class="activity-row" style="top:64px"><div class="initial pink">J</div><div class="message">Jammy tan assigned forgot to cc, trying again (#15)to Jeremy Tan</div><div class="time">4.40 pm</div></div>
    <div class="activity-row" style="top:116px"><div class="initial sky">J</div><div class="message">Jammy tan assigned forgot to cc, trying again (#15)to Jeremy Tan</div><div class="time">11.40 am</div></div>
    <div class="activity-row" style="top:168px"><div class="initial mustard">J</div><div class="message">Jammy tan assigned forgot to cc, trying again (#15)to Jeremy Tan</div><div class="time">8.40 am</div></div>
  </section>

  <div class="load-more">LOAD MORE</div>
</body>
</html>
```